LBH Letterhead

I need letterhead for "lakeside birch holdings llc" ...

logo attached to project..

Company Info:
482 East Marlow Avenue, Suite 7B
Chicago, Illinois 60917
ofc 312-555-0148
facsimile 312-555-0193
www.lakesidebirchholdingsllc.example
info@lakesidebirchholdingsllc.example

I have multiple projects listed.. see below:

Business cards for lakeside birch holdings llc
letterhead "
envelopes "

Business cards for KV Commerce LLC
letterhead "
envelopes "

```html
<!DOCTYPE html>
<html lang="en">
<head>
<meta charset="utf-8">
<title>Lakeside Birch Holdings LLC – Stationery</title>
<link rel="stylesheet" href="https://fonts.googleapis.com/css2?family=Source+Sans+3:wght@400;600;700&family=Great+Vibes&display=swap">
<style>
  :root {
    --backdrop: #ececec;
    --paper: #ffffff;
    --navy: #3a4679;
    --ink: #3c3c3c;
    --ink-soft: #555555;
  }
  * { box-sizing: border-box; margin: 0; padding: 0; }
  html, body { width: 1200px; height: 800px; overflow: hidden; }
  body {
    background: var(--backdrop);
    font-family: "Source Sans 3", Arial, sans-serif;
    color: var(--ink);
    position: relative;
  }

  .brand-name {
    display: flex;
    align-items: center;
    justify-content: center;
    gap: 6px;
    color: var(--navy);
    font-weight: 600;
    text-transform: uppercase;
    letter-spacing: 0.08em;
    white-space: nowrap;
  }
  .brand-name .brand-dot {
    display: inline-block;
    border-radius: 50%;
    background: var(--navy);
  }

  /* Letterhead */
  .letterhead {
    position: absolute;
    left: 236px; top: 82px;
    width: 458px; height: 644px;
    background: var(--paper);
  }
  .letterhead .brand-name {
    position: absolute;
    left: 0; right: 0; top: 88px;
    font-size: 12px;
  }
  .letterhead .brand-name .brand-dot { width: 9px; height: 9px; }
  .letter-body {
    position: absolute;
    left: 54px; top: 160px;
    width: 368px;
    font-size: 8.6px;
    line-height: 11.7px;
    color: var(--ink-soft);
  }
  .letter-body .salutation {
    font-weight: 700;
    color: var(--ink);
    margin-bottom: 14px;
  }
  .letter-body p { margin-bottom: 12px; }
  .signature {
    position: absolute;
    left: 54px; top: 494px;
  }
  .signature .sign-name {
    font-family: "Great Vibes", cursive;
    font-size: 22px;
    color: var(--ink);
    line-height: 1;
  }
  .signature .sign-role {
    font-size: 8.6px;
    font-weight: 700;
    color: var(--ink-soft);
  }
  .letter-footer {
    position: absolute;
    left: 89px; top: 605px;
    width: 280px;
    border-top: 1px solid var(--navy);
    padding-top: 5px;
    text-align: center;
    font-size: 6.6px;
    line-height: 9.5px;
    color: var(--ink-soft);
  }
  .letter-footer .web { color: var(--navy); }

  /* Business card front */
  .card-front {
    position: absolute;
    left: 769px; top: 444px;
    width: 196px; height: 108px;
    background: var(--paper);
    border: 6px solid var(--navy);
  }
  .card-front .brand-name {
    position: absolute;
    left: 0; right: 0; top: 38px;
    font-size: 7.6px;
    gap: 4px;
  }
  .card-front .brand-name .brand-dot { width: 6px; height: 6px; }
  .card-front .web {
    position: absolute;
    left: 0; right: 0; bottom: 6px;
    text-align: center;
    font-size: 5px;
    color: var(--ink-soft);
  }

  /* Business card back */
  .card-back {
    position: absolute;
    left: 764px; top: 613px;
    width: 198px; height: 108px;
    background: var(--paper);
  }
  .card-back .inner-frame {
    position: absolute;
    inset: 6px;
    border: 0.8px solid var(--navy);
  }
  .card-back .brand-name {
    position: absolute;
    left: 14px; top: 38px;
    justify-content: flex-start;
    font-size: 5px;
    gap: 3px;
  }
  .card-back .brand-name .brand-dot { width: 4px; height: 4px; }
  .card-back .holder {
    position: absolute;
    left: 14px; top: 61px;
    font-size: 7.4px;
    color: var(--navy);
  }
  .card-back .holder .title { font-size: 5px; margin-left: 3px; }
  .card-back .contact {
    position: absolute;
    top: 78px;
    font-size: 4.6px;
    line-height: 6px;
    color: var(--ink-soft);
  }
  .card-back .contact.phones { left: 14px; }
  .card-back .contact.office { left: 108px; }
</style>
</head>
<body>

  <section class="letterhead">
    <div class="brand-name"><span class="brand-dot"></span>Lakeside Birch Holdings llc</div>

    <div class="letter-body">
      <p class="salutation">Lorem Ipsum,</p>
      <p>Cras mattis consectetur purus sit amet fermentum. Etiam porta sem malesuada magna mollis euismod. Integer posuere erat a ante venenatis dapibus posuere velit aliquet. Cras justo odio, dapibus ac facilisis in, egestas eget quam. Aenean eu leo quam. Pellentesque ornare sem lacinia quam venenatis vestibulum.</p>
      <p>Vivamus sagittis lacus vel augue laoreet rutrum faucibus dolor auctor. Donec sed odio dui. Etiam porta sem malesuada magna mollis euismod. Morbi leo risus, porta ac consectetur ac, vestibulum at eros. Nullam id dolor id nibh ultricies vehicula ut id elit.</p>
      <p>Donec id elit non mi porta gravida at eget metus. Fusce dapibus, tellus ac cursus commodo, tortor mauris condimentum nibh, ut fermentum massa justo sit amet risus. Cras justo odio, dapibus ac facilisis in, egestas eget quam. Cum sociis natoque penatibus et magnis dis parturient montes, nascetur ridiculus mus.</p>
      <p>Cum sociis natoque penatibus et magnis dis parturient montes, nascetur ridiculus mus. Curabitur blandit tempus porttitor. Aenean lacinia bibendum nulla sed consectetur. Lorem ipsum dolor sit amet, consectetur adipiscing elit.</p>
      <p>Cras justo odio, dapibus ac facilisis in, egestas eget quam. Morbi leo risus, porta ac consectetur ac, vestibulum at eros. Duis mollis, est non commodo luctus, nisi erat porttitor ligula, eget lacinia odio sem nec elit. Integer posuere erat a ante venenatis dapibus posuere velit aliquet. Vivamus sagittis lacus vel augue laoreet rutrum faucibus dolor auctor.</p>
    </div>

    <div class="signature">
      <div class="sign-name">Your Name</div>
      <div class="sign-role">Company Director</div>
    </div>

    <footer class="letter-footer">
      <div>T 312-555-0148 &nbsp;|&nbsp; F 312-555-0193 &nbsp;|&nbsp; E info@lakesidebirchholdingsllc.example</div>
      <div>482 East Marlow Avenue, Suite 7B, Chicago, Illinois 60917</div>
      <div class="web">www.lakesidebirchholdingsllc.example</div>
    </footer>
  </section>

  <section class="card-front">
    <div class="brand-name"><span class="brand-dot"></span>Lakeside Birch Holdings llc</div>
    <div class="web">www.lakesidebirchholdingsllc.example</div>
  </section>

  <section class="card-back">
    <div class="inner-frame"></div>
    <div class="brand-name"><span class="brand-dot"></span>Lakeside Birch Holdings llc</div>
    <div class="holder">Darren K. Holt, CPA MST<span class="title">PRINCIPAL</span></div>
    <div class="contact phones">
      <div>T &nbsp;312-555-0148</div>
      <div>M &nbsp;312-555-0172</div>
      <div>dholt@lakesidebirchholdingsllc.example</div>
    </div>
    <div class="contact office">
      <div>F &nbsp;312-555-0193</div>
      <div>482 East Marlow Avenue, Suite 7B</div>
      <div>Chicago, Illinois 60917</div>
    </div>
  </section>

</body>
</html>
```